**** Business card design for LumaSoft ****

For my ICT company LumaSoft I need I need a business card design.

We design, build and host web-applications and we have our own CMS product.

Some good examples are attached.

The information should be:
Joren Velthuis
Managing director
E: j.velthuis@lumasoft-example.nl
M: +31(0)6 57182604
T: +31(0)40 7214589
W: www.lumasoft-example.nl

Address:
Pieter Dommelenlaan 27
5612 KT Eindhoven

Requirements
Must have
• - Use logo (see attachments)
- Double sided
- Distinctive
Nice to have
• - Place for a statement on the back-side: "Designed with knowledge, built with passion"
- HTML code (or Pagecraft)
- Dark (black or dark-gray) side
- Small simple images for telephone, e-mail en Url.
- QR code (only if not disturbing), not required, just an option

```html
<!DOCTYPE html>
<html lang="en">
<head>
<meta charset="utf-8">
<title>LumaSoft Stationery</title>
<link href="https://fonts.googleapis.com/css2?family=PT+Sans:wght@400;700&display=swap" rel="stylesheet">
<style>
  :root {
    --canvas: #ffffff;
    --card-black: #0b0b0b;
    --yellow: #f2e600;
    --yellow-light: #fbf59a;
    --yellow-deep: #e3d800;
    --rule: #6e6e6e;
    --ink: #1c1c1c;
    --white: #ffffff;
    --brand-grey: #5d6f80;
    --brand-grey-light: #9fb0bf;
    --brand-blue: #3f83c6;
  }
  html, body {
    margin: 0;
    padding: 0;
    width: 1016px;
    height: 1200px;
    overflow: hidden;
    background: var(--canvas);
    font-family: "PT Sans", "Myriad Pro", sans-serif;
  }
  .sheet {
    position: relative;
    width: 931px;
    height: 1100px;
    transform: scale(1.0913);
    transform-origin: 0 0;
  }

  /* Letterhead */
  .letterhead {
    position: absolute;
    left: 0; top: 0;
    width: 849px; height: 1099px;
    border: 1px solid var(--rule);
    border-top: none;
    background: var(--canvas);
    overflow: hidden;
  }
  .letterhead__band {
    position: absolute;
    left: 0; right: 0; bottom: 0;
    height: 150px;
    background: linear-gradient(to bottom, var(--canvas) 0%, var(--yellow-light) 55%, var(--yellow) 100%);
  }
  .letterhead__footer {
    position: absolute;
    left: 0; width: 850px;
    top: 895px;
    text-align: center;
  }

  /* Brand lockup */
  .brand {
    display: inline-flex;
    align-items: center;
    gap: 10px;
  }
  .brand__mark {
    width: 50px; height: 50px;
    border-radius: 50%;
    background: var(--brand-blue);
  }
  .brand__name {
    font-size: 30px;
    font-weight: 400;
    letter-spacing: .5px;
    color: var(--brand-grey);
  }
  .brand--on-dark .brand__name { color: var(--brand-grey-light); }

  .contact-block {
    margin-top: 12px;
    font-size: 14px;
    line-height: 20px;
    color: var(--ink);
  }

  /* Business cards */
  .card {
    position: absolute;
    top: 120px;
    width: 351px; height: 200px;
    border-radius: 18px;
    background: var(--card-black);
    overflow: hidden;
  }
  .card--front { left: 77px; }
  .card--back { left: 452px; }
  .card__panel {
    position: absolute;
    top: 0; bottom: 0;
    width: 110px;
    background: linear-gradient(to bottom, var(--yellow) 0%, var(--yellow-deep) 100%);
  }
  .card--front .card__panel { right: 0; }
  .card--back .card__panel { left: 0; }
  .card--front .brand {
    position: absolute;
    left: 30px; top: 74px;
  }
  .card--front .brand__mark { width: 46px; height: 46px; }
  .card--front .brand__name { font-size: 26px; }

  .card__identity {
    position: absolute;
    right: 16px; top: 14px;
    text-align: right;
    color: var(--white);
  }
  .card__name { font-size: 11px; line-height: 14px; }
  .card__role { font-size: 7.5px; line-height: 10px; }
  .card__details {
    position: absolute;
    left: 207px; top: 118px;
    font-size: 7.5px;
    line-height: 10px;
    color: var(--white);
    white-space: nowrap;
  }

  /* Envelope */
  .envelope {
    position: absolute;
    left: 32px; top: 367px;
    width: 899px; height: 499px;
  }
  .envelope__flap {
    position: absolute;
    left: 0; top: 0;
    width: 899px; height: 100px;
  }
  .envelope__body {
    position: absolute;
    left: 0; top: 100px;
    width: 897px; height: 398px;
    border: 1px solid var(--rule);
    background: var(--canvas);
    overflow: hidden;
  }
  .envelope__band {
    position: absolute;
    left: 0; right: 0; bottom: 0;
    height: 130px;
    background: linear-gradient(to bottom, var(--canvas) 0%, var(--yellow-light) 60%, var(--yellow) 100%);
  }
  .envelope__footer {
    position: absolute;
    left: 0; right: 0;
    top: 218px;
    text-align: center;
  }
</style>
</head>
<body>
<div class="sheet">

  <section class="letterhead">
    <div class="letterhead__band" role="img" aria-label="Yellow decorative band"></div>
    <div class="letterhead__footer">
      <div class="brand"><span class="brand__mark"></span><span class="brand__name">LumaSoft</span></div>
      <div class="contact-block">
        Address: Pieter Dommelenlaan 27, 5612 KT Eindhoven<br>
        Cell: +31(0)6 57182604 Ph: +31(0)40 7214589<br>
        Email: j.velthuis@lumasoft-example.nl<br>
        www.lumasoft-example.nl
      </div>
    </div>
  </section>

  <article class="card card--front">
    <div class="brand brand--on-dark"><span class="brand__mark"></span><span class="brand__name">LumaSoft</span></div>
    <div class="card__panel" role="img" aria-label="Yellow decorative panel"></div>
  </article>

  <article class="card card--back">
    <div class="card__panel" role="img" aria-label="Yellow decorative panel"></div>
    <div class="card__identity">
      <div class="card__name">Joren Velthuis</div>
      <div class="card__role">Managing Director</div>
    </div>
    <div class="card__details">
      Pieter Dommelenlaan 27<br>
      5612 KT Eindhoven<br>
      +31(0)6 57182604<br>
      +31(0)40 7214589<br>
      Email: j.velthuis@lumasoft-example.nl<br>
      www.lumasoft-example.nl
    </div>
  </article>

  <section class="envelope">
    <svg class="envelope__flap" viewBox="0 0 899 100" role="img" aria-label="Envelope flap in yellow">
      <defs>
        <linearGradient id="flap-fill" x1="0" y1="0" x2="0" y2="1">
          <stop offset="0" stop-color="#f2e600"/>
          <stop offset="1" stop-color="#e6da00"/>
        </linearGradient>
      </defs>
      <polygon points="0,100 36,0 863,0 899,100" fill="url(#flap-fill)" stroke="#6e6e6e" stroke-width="1"/>
    </svg>
    <div class="envelope__body">
      <div class="envelope__band" role="img" aria-label="Yellow decorative band"></div>
      <div class="envelope__footer">
        <div class="brand"><span class="brand__mark"></span><span class="brand__name">LumaSoft</span></div>
        <div class="contact-block">
          Address: Pieter Dommelenlaan 27, 5612 KT Eindhoven<br>
          Cell: +31(0)6 57182604 Ph: +31(0)40 7214589<br>
          Email: j.velthuis@lumasoft-example.nl<br>
          www.lumasoft-example.nl
        </div>
      </div>
    </div>
  </section>

</div>
</body>
</html>
```